Business Card for beauty technology startup

Design Glowmi Business Card for a Beauty, based on the website identity and colors (https://www.glowmi-example.com).
Glowmi is a beauty tech startup that gathers helpful product info for beauty lovers and consumers (such as availability on stores, price range and product reviews) for makeup products. The card design must be young, colorful but clean, and very modern.

Target Market(s)

woman, 15-35

Industry/Entity Type

Cosmetics

Contact Information for Business Card

Full Name, address, phone

Font styles to use
Other font styles liked:
• Advent Pro

Colors
e34297
86cfc6
ffffff
5c5c5c
e8e8e8
e667a6
b2b2b2

Requirements
Must have
• One full colored side with a creative design and another with card info
• Use Color palette: #95C5C5 and/or #D38AA5
• Use fonts: Advent Pro
• Use website identity: https://www.glowmi-example.com
Nice to have
• If needed extra font: Roboto

```html
<!DOCTYPE html>
<html lang="en">
<head>
<meta charset="utf-8">
<title>Glowmi Business Card</title>
<link href="https://fonts.googleapis.com/css2?family=Advent+Pro:wght@300;400&family=Roboto:wght@400;500&family=Open+Sans:wght@400&display=swap" rel="stylesheet">
<style>
  :root {
    --pink: #e0197d;
    --pink-soft: #e34297;
    --ink: #1f1f1f;
    --paper: #f4f4f2;
    --slate: #4a4a4a;
    --backdrop: #e8e8e8;
  }
  * { margin: 0; padding: 0; box-sizing: border-box; }
  html, body { width: 1200px; height: 1021px; overflow: hidden; background: var(--backdrop); }
  .canvas { position: relative; width: 1200px; height: 1021px; }
  .card {
    position: absolute; width: 560px; height: 320px;
    border-bottom: 6px solid var(--pink);
    box-shadow: 0 14px 30px rgba(0,0,0,0.18);
  }
  .card--front { left: 70px; top: 90px; background: var(--paper); }
  .card--back { left: 570px; top: 580px; background: var(--slate); }

  .brand { position: absolute; display: flex; align-items: center; color: var(--pink); font-family: "Advent Pro", sans-serif; font-weight: 300; }
  .brand__dot { border: 2px solid var(--pink); border-radius: 50%; }
  .card--front .brand { right: 40px; top: 36px; gap: 14px; font-size: 38px; letter-spacing: 6px; }
  .card--front .brand__dot { width: 40px; height: 40px; }

  .social { position: absolute; right: 46px; top: 100px; display: flex; gap: 22px; }
  .social__item { width: 12px; height: 12px; background: var(--pink); border-radius: 2px; }

  .identity { position: absolute; left: 34px; top: 140px; padding-left: 16px; border-left: 9px solid var(--pink); }
  .identity__name { font-family: "Roboto", sans-serif; font-weight: 500; font-size: 25px; color: var(--ink); line-height: 1.05; }
  .identity__title { font-family: "Roboto", sans-serif; font-size: 15px; color: var(--pink); margin-top: 2px; }

  .url { font-family: "Roboto", sans-serif; color: var(--pink); }
  .card--front .url { position: absolute; right: 40px; top: 196px; font-size: 15px; letter-spacing: 0.3px; }

  .contact { position: absolute; left: 170px; top: 226px; font-family: "Open Sans", sans-serif; font-size: 14px; color: var(--ink); line-height: 1.3; }
  .contact__row { display: flex; align-items: flex-start; gap: 10px; margin-bottom: 6px; }
  .contact__icon { width: 13px; height: 13px; flex: none; margin-top: 2px; fill: var(--pink); }

  .card--back .brand { left: 50%; top: 104px; transform: translateX(-50%); gap: 22px; font-size: 64px; letter-spacing: 10px; white-space: nowrap; }
  .card--back .brand__dot { width: 76px; height: 76px; }
  .card--back .url { position: absolute; left: 0; right: 0; top: 214px; text-align: center; font-size: 15px; letter-spacing: 1px; }
</style>
</head>
<body>
<main class="canvas">
  <section class="card card--front">
    <div class="brand"><span class="brand__dot"></span><span class="brand__name">GLOWMI</span></div>
    <div class="social" aria-label="Social links">
      <span class="social__item"></span><span class="social__item"></span><span class="social__item"></span><span class="social__item"></span>
    </div>
    <div class="identity">
      <p class="identity__name">Your Name</p>
      <p class="identity__title">Job Title</p>
    </div>
    <p class="url">www.glowmi-example.com</p>
    <div class="contact">
      <div class="contact__row">
        <svg class="contact__icon" viewBox="0 0 16 16"><path d="M3 1h3l1.5 4-2 1.3a9 9 0 0 0 4.2 4.2L11 8.5l4 1.5v3a2 2 0 0 1-2 2A13 13 0 0 1 1 3a2 2 0 0 1 2-2z"/></svg>
        <span>000 000 0000</span>
      </div>
      <div class="contact__row">
        <svg class="contact__icon" viewBox="0 0 16 16"><path d="M8 0a5.5 5.5 0 0 0-5.5 5.5C2.5 10 8 16 8 16s5.5-6 5.5-10.5A5.5 5.5 0 0 0 8 0zm0 8a2.5 2.5 0 1 1 0-5 2.5 2.5 0 0 1 0 5z"/></svg>
        <span>1450 Linden Ave, suite 310<br>Harbor Falls, Texas 78020</span>
      </div>
    </div>
  </section>

  <section class="card card--back">
    <div class="brand"><span class="brand__dot"></span><span class="brand__name">GLOWMI</span></div>
    <p class="url">www.glowmi-example.com</p>
  </section>
</main>
</body>
</html>
```